Conceptual Model Diagram for Replacing Medication with Behavior to Support Weight Loss Maintenance

Design a figure of a conceptual model that needs to be inserted into a word document for a QDV grant. This conceptual model illustrates how behavioral strategies can replace the regulatory functions lost after AOM discontinuation. The intervention targets three core vulnerabilities—appetite resurgence, metabolic inflexibility, and suboptimal mindstate—through the domains of Food, Physical Activity, and Mind. Sustained weight loss maintenance occurs at the intersection of these domains. The intervention is delivered within a design framework that makes behaviors easier to perform, aligns them with identity, and reinforces them through virtual support and community, ensuring real-world feasibility and long-term adherence.
Target Market(s)
QDV reviewers
Industry/Entity Type
academic
Font styles to use
Other font styles liked:
- arial
Requirements
Must have
- see my attached description

```html
<!DOCTYPE html>
<html lang="en">
<head>
<meta charset="utf-8">
<title>Conceptual Model for Replacing Medication with Behavior to Support Weight Loss Maintenance</title>
<link rel="stylesheet" href="https://fonts.googleapis.com/css2?family=Arimo:wght@400;700&family=Ubuntu:wght@400;500&family=Mulish:wght@500;700&display=swap">
<style>
  :root {
    --navy: #1d5590;
    --gold: #fbc531;
    --teal: #43aeaa;
    --teal-deep: #23958f;
    --red: #e0395a;
    --red-deep: #c42a4b;
    --yellow: #f9c62f;
    --yellow-deep: #eeae1c;
    --ink: #1a1a1a;
    --grey: #6b6b6b;
    --white: #ffffff;
  }
  * { margin: 0; padding: 0; box-sizing: border-box; }
  html, body { width: 1200px; height: 675px; overflow: hidden; background: var(--white); }
  .canvas { position: relative; width: 1200px; height: 675px; overflow: hidden; background: var(--white); font-family: "Arimo", Arial, sans-serif; }

  .brand { position: absolute; left: 69px; top: 67px; display: flex; align-items: center; gap: 10px; color: var(--grey); }
  .brand-mark { width: 14px; height: 14px; background: var(--grey); }
  .brand-acronym { font-size: 30px; font-weight: 700; letter-spacing: -0.5px; }
  .brand-name { font-size: 20px; font-weight: 700; margin-left: 4px; }

  .title-band { position: absolute; left: 0; top: 194px; width: 1200px; height: 239px; background: var(--navy); }
  .title { position: absolute; left: 69px; top: 236px; color: var(--white); font-size: 32.5px; font-weight: 400; line-height: 39px; }
  .title-accent { display: block; margin-top: 5px; color: var(--gold); font-weight: 700; font-size: 33px; }

  .summary { position: absolute; left: 69px; top: 476px; width: 397px; font-size: 14.6px; line-height: 18px; color: var(--ink); text-align: justify; }

  .model { position: absolute; left: 537px; top: 69px; width: 544px; height: 544px; }
  .ring-label { font-family: "Ubuntu", sans-serif; fill: var(--white); }
  .ring-head { font-size: 38px; font-weight: 500; }
  .ring-head-compact { font-size: 34px; font-weight: 500; }
  .ring-sub { font-size: 24px; }
  .ring-sub-compact { font-size: 23px; }
  .venn-label { font-family: "Mulish", sans-serif; font-weight: 700; fill: var(--white); font-size: 20px; }
  .venn-core { font-family: "Mulish", sans-serif; font-weight: 700; fill: #333; font-size: 12.5px; }
  .note { font-family: "Mulish", sans-serif; font-weight: 500; font-size: 18px; }
</style>
</head>
<body>
<div class="canvas">
  <div class="brand">
    <span class="brand-mark"></span>
    <span class="brand-acronym">QDV</span>
    <span class="brand-name">Qualis Directorate of Vitality</span>
  </div>

  <div class="title-band"></div>
  <h1 class="title">Conceptual Model for<br>Replacing Medication with<br>Behavior to Support<span class="title-accent">Weight Loss Maintenance</span></h1>

  <p class="summary">This model shows how behavioral strategies can restore regulation after AOM ends, targeting appetite resurgence, metabolic inflexibility, and suboptimal mindstate through focused interventions in Food, Physical Activity, and Mind.</p>

  <svg class="model" viewBox="860 110 870 870" role="img" aria-label="Conceptual model diagram: Food, Mind and Physical Activity overlapping at sustained weight loss maintenance, surrounded by three design principles">
    <defs>
      <filter id="disc-shadow" x="-20%" y="-20%" width="140%" height="140%">
        <feDropShadow dx="0" dy="6" stdDeviation="14" flood-color="#000" flood-opacity="0.18"/>
      </filter>
      <clipPath id="clip-food"><circle cx="1290" cy="450" r="132"/></clipPath>
      <clipPath id="clip-mind"><circle cx="1213" cy="590" r="130"/></clipPath>
      <clipPath id="clip-activity"><circle cx="1368" cy="590" r="130"/></clipPath>
      <!-- text guides -->
      <path id="guide-easy" d="M 1033.6 304.4 A 350 350 0 0 1 1566 318"/>
      <path id="guide-easy-1" d="M 1262.3 171.4 A 370 370 0 0 1 1600 300"/>
      <path id="guide-easy-2" d="M 1264.9 197.3 A 344 344 0 0 1 1570 330"/>
      <path id="guide-identity" d="M 981.2 343.9 A 370 370 0 0 0 1230.8 904.4"/>
      <path id="guide-identity-2" d="M 910.8 635.8 A 396 396 0 0 0 1097 882.9"/>
      <path id="guide-virtual" d="M 1150 895 A 385 385 0 0 0 1680 540"/>
      <path id="guide-virtual-1" d="M 1645 560 A 350 350 0 0 0 1560 300"/>
      <path id="guide-virtual-2" d="M 1674 560 A 379 379 0 0 0 1590 300"/>
    </defs>

    <circle cx="1295" cy="540" r="425" fill="#fff" filter="url(#disc-shadow)"/>

    <!-- ring segments -->
    <path d="M 1009 295 A 378 378 0 0 1 1576 287" fill="none" stroke="var(--teal)" stroke-width="76"/>
    <path d="M 1576 287 A 378 378 0 0 1 1143 886" fill="none" stroke="var(--yellow)" stroke-width="76"/>
    <path d="M 1143 886 A 378 378 0 0 1 1009 295" fill="none" stroke="var(--red)" stroke-width="76"/>
    <circle cx="1295" cy="540" r="322" fill="#fff"/>
    <circle cx="1295" cy="540" r="312" fill="none" stroke="#eef1f3" stroke-width="6"/>

    <!-- ring text -->
    <text class="ring-label ring-head"><textPath href="#guide-easy">Make it Easy:</textPath></text>
    <text class="ring-label ring-sub"><textPath href="#guide-easy-1">habits, routines,</textPath></text>
    <text class="ring-label ring-sub"><textPath href="#guide-easy-2">environment, low friction</textPath></text>
    <text class="ring-label"><textPath href="#guide-identity"><tspan class="ring-head-compact">Align with Identity: </tspan><tspan class="ring-sub-compact">self-concept, Maintain IT model,</tspan></textPath></text>
    <text class="ring-label ring-sub-compact"><textPath href="#guide-identity-2">internalization</textPath></text>
    <text class="ring-label ring-head"><textPath href="#guide-virtual">Virtual Support and Social Connection:</textPath></text>
    <text class="ring-label ring-sub"><textPath href="#guide-virtual-1">accessibility, community,</textPath></text>
    <text class="ring-label ring-sub"><textPath href="#guide-virtual-2">shared accountability</textPath></text>

    <!-- venn domains -->
    <circle cx="1290" cy="450" r="132" fill="var(--teal)"/>
    <circle cx="1213" cy="590" r="130" fill="var(--red)"/>
    <circle cx="1368" cy="590" r="130" fill="var(--yellow)"/>
    <g clip-path="url(#clip-food)">
      <circle cx="1213" cy="590" r="130" fill="var(--red-deep)" role="img" aria-label="Mindfulness icon area"/>
      <circle cx="1368" cy="590" r="130" fill="var(--teal-deep)" role="img" aria-label="Healthy meal icon area"/>
    </g>
    <g clip-path="url(#clip-mind)">
      <circle cx="1368" cy="590" r="130" fill="var(--yellow-deep)" role="img" aria-label="Active movement icon area"/>
      <g clip-path="url(#clip-activity)">
        <circle cx="1290" cy="450" r="132" fill="#fff"/>
      </g>
    </g>
    <g fill="none" stroke="#fff" stroke-width="7">
      <circle cx="1290" cy="450" r="132"/>
      <circle cx="1213" cy="590" r="130"/>
      <circle cx="1368" cy="590" r="130"/>
    </g>

    <text class="venn-label" x="1290" y="409" text-anchor="middle">FOOD</text>
    <text class="venn-label" x="1160" y="611" text-anchor="middle">Mind</text>
    <text class="venn-label" x="1416" y="594" text-anchor="middle">Physical</text>
    <text class="venn-label" x="1416" y="614" text-anchor="middle">Activity</text>
    <text class="venn-core" text-anchor="middle"><tspan x="1291" y="529">Sustained</tspan><tspan x="1291" y="545">Weight Loss</tspan><tspan x="1291" y="561">Maintenance</tspan></text>

    <!-- vulnerabilities -->
    <text class="note" fill="var(--teal)" text-anchor="middle"><tspan x="1283" y="267">Appetite</tspan><tspan x="1283" y="290">Resurgence</tspan></text>
    <path d="M 1283 298 V 356" stroke="var(--teal)" stroke-width="2" fill="none"/>
    <path d="M 1278 352 L 1283 361 L 1288 352 Z" fill="var(--teal)"/>

    <text class="note" fill="var(--red)" text-anchor="middle"><tspan x="1033" y="539">Suboptimal</tspan><tspan x="1033" y="562">Mindstate</tspan></text>
    <path d="M 1033 570 V 607 H 1120" stroke="#f0892d" stroke-width="2" fill="none"/>
    <path d="M 1117 602 L 1126 607 L 1117 612 Z" fill="#f0892d"/>

    <text class="note" fill="var(--yellow)" text-anchor="middle"><tspan x="1550" y="539">Appetite</tspan><tspan x="1550" y="562">Resurgence</tspan></text>
    <path d="M 1560 570 V 607 H 1474" stroke="#f0892d" stroke-width="2" fill="none"/>
    <path d="M 1477 602 L 1468 607 L 1477 612 Z" fill="#f0892d"/>
  </svg>
</div>
</body>
</html>
```